Business card for our large format printing and installation business

We want a professional looking business card for our business. We manufacture and install Signs.

On the back of the card add this info
Large Format Graphics Printing & Installations, Event Graphics, Banners, Posters, Vehicle Fleet Graphics, Boat Wraps, Wall Murals, Decals,Displays,Signs,Plaques,Digital Signs

On the Front of the card add the Tallowfern Signs logo, plus On the back of the card add the Orange Tallowfern Wraps logo. The 2 vector logos are attached to the design brief.

Target Market(s)

Local business owners

Contact Information for Business Card

Colors
f37122
f68d4e
f9ba93

Requirements
Must have
• On the Front of the card add the Tallowfern Signs logo, plus On the back of the card add the Orange Tallowfern Wraps logo. The 2 vector logos are attached to the design brief.

```html
<!DOCTYPE html>
<html lang="en">
<head>
<meta charset="utf-8">
<title>Tallowfern Signs – Business Card</title>
<link href="https://fonts.googleapis.com/css2?family=Roboto:wght@400;500;700;900&display=swap" rel="stylesheet">
<style>
  :root{
    --bg:#2b2b2b;
    --card:#ffffff;
    --ink:#1a1a1a;
    --yellow:#f9e22b;
    --amber:#fbb829;
    --orange:#f37122;
    --orange-mid:#f68d4e;
    --orange-soft:#f9ba93;
    --map:#e9eaec;
    --ribbon:#1c1c1c;
    --ribbon-fold:#000000;
  }
  *{box-sizing:border-box;margin:0;padding:0}
  html,body{width:1200px;height:900px;overflow:hidden}
  body{background:var(--bg);font-family:"Roboto",Arial,sans-serif;color:var(--ink);position:relative}

  .card{position:absolute;width:540px;height:308px;border-radius:18px;background:var(--card);overflow:hidden;box-shadow:0 10px 28px rgba(0,0,0,.45)}

  /* Front card */
  .card-front{left:60px;top:90px}
  .brand{display:flex;align-items:center;gap:10px;font-weight:900;color:var(--amber);letter-spacing:.3px;white-space:nowrap}
  .card-front .brand{position:absolute;left:0;right:0;top:92px;justify-content:center;font-size:48px;gap:12px}
  .brand-dot{width:18px;height:18px;border-radius:50%;background:var(--orange);flex:none}
  .card-front .brand-dot{width:30px;height:30px}
  .service-band{position:absolute;left:0;right:0;bottom:36px;height:24px;display:flex;align-items:center;justify-content:center;font-size:12.5px;color:var(--ink)}
  .service-line{position:absolute;left:0;right:0;bottom:32px;height:2px;background:var(--amber)}
  .service-stripe{position:absolute;left:0;right:0;bottom:14px;height:16px;background:linear-gradient(180deg,var(--yellow),var(--orange))}

  /* Back card */
  .card-back{left:600px;top:500px}
  .world-map{position:absolute;left:20px;top:20px;width:300px;height:250px;border-radius:40% 50% 45% 35%;background:radial-gradient(ellipse at 40% 45%,var(--map),rgba(233,234,236,0) 70%)}
  .card-back .brand{position:absolute;left:30px;top:104px;font-size:22px}
  .color-panel{position:absolute;inset:0;background:linear-gradient(160deg,var(--yellow) 0%,var(--amber) 45%,var(--orange-mid) 100%);clip-path:polygon(44% 0,100% 0,100% 100%,63% 100%)}
  .name-ribbon{position:absolute;left:228px;top:34px;width:232px;height:56px;background:var(--ribbon);color:#fff;display:flex;flex-direction:column;align-items:center;justify-content:center}
  .name-ribbon .name{font-size:17px;font-weight:700}
  .name-ribbon .role{font-size:9px;margin-top:2px}
  .ribbon-fold{position:absolute;left:228px;top:90px}
  .address{position:absolute;right:28px;top:186px;width:190px;text-align:center;font-size:12px;line-height:1.35;color:var(--ink)}
  .address svg{display:block;margin:0 auto 6px}
  .contact-list{position:absolute;left:36px;bottom:26px;list-style:none;display:flex;flex-direction:column;gap:7px}
  .contact-list li{display:flex;align-items:center;gap:10px;font-size:13px}
  .contact-icon{width:18px;height:18px;background:var(--ink);display:flex;align-items:center;justify-content:center;flex:none}
</style>
</head>
<body>

<section class="card card-front" aria-label="Business card front">
  <div class="brand"><span class="brand-dot"></span>Tallowfern Signs</div>
  <div class="service-band">Vehicle Wraps ~ Wall Murals ~ Fleet graphics ~ Event graphics,etc</div>
  <div class="service-line"></div>
  <div class="service-stripe"></div>
</section>

<section class="card card-back" aria-label="Business card back">
  <div class="world-map" role="img" aria-label="Faint world map backdrop"></div>
  <div class="color-panel"></div>
  <div class="brand"><span class="brand-dot"></span>Tallowfern Wraps</div>
  <svg class="ribbon-fold" width="26" height="22" viewBox="0 0 26 22"><polygon points="0,0 26,0 26,22" fill="var(--ribbon-fold)"/></svg>
  <div class="name-ribbon">
    <span class="name">Marco Delgado</span>
    <span class="role">CEO</span>
  </div>
  <div class="address">
    <svg width="12" height="16" viewBox="0 0 12 16"><path d="M6 0a6 6 0 0 0-6 6c0 4.5 6 10 6 10s6-5.5 6-10a6 6 0 0 0-6-6zm0 8.5A2.5 2.5 0 1 1 6 3.5a2.5 2.5 0 0 1 0 5z" fill="var(--ink)"/></svg>
    1480 Harbor Mill Road #4<br>Seabrook Point, FL 33021
  </div>
  <ul class="contact-list">
    <li><span class="contact-icon"><svg width="11" height="11" viewBox="0 0 12 12"><path d="M2.5 0.5l2 2.5-1.2 1.4a7 7 0 0 0 4.3 4.3L9 7.5l2.5 2-1.3 2C5 11 1 7 0.5 1.8z" fill="#fff"/></svg></span>786-555-0142</li>
    <li><span class="contact-icon"><svg width="11" height="11" viewBox="0 0 12 12"><rect x="1" y="4" width="10" height="7" rx="1" fill="#fff"/><rect x="2" y="1" width="8" height="3" rx="1" fill="#fff"/></svg></span>954-555-0187</li>
    <li><span class="contact-icon"><svg width="12" height="10" viewBox="0 0 12 10"><rect x="0.5" y="0.5" width="11" height="9" fill="none" stroke="#fff"/><path d="M0.5 0.5l5.5 5 5.5-5" fill="none" stroke="#fff"/></svg></span>marco@tallowfern.net</li>
    <li><span class="contact-icon"><svg width="12" height="12" viewBox="0 0 12 12"><circle cx="6" cy="6" r="5" fill="none" stroke="#fff"/><path d="M1 6h10M6 1c-3 3-3 7 0 10M6 1c3 3 3 7 0 10" fill="none" stroke="#fff" stroke-width=".8"/></svg></span>www.tallowfernwraps.com</li>
  </ul>
</section>

</body>
</html>
```